graphic showing our process of education as a process called a pipeline

Also see my updated comments on discussion section.
Title of the graphic needs to be:
TITLE = The KELIMO Strategic Leadership Pipeline = larger, bold heading
SUB-TITLE = Developing a steady flow of servant leaders for Tanzania's future = under title; smaller font
change the text for each of the 7 steps to match the outcomes listed on the newly attached PDF (strategic pipeline 11x17)
Pipe should be straight or mostly straight.
Pipe should not be in a strong or dark color.
Any icons or symbols should be simple and professional, not like cartoon or childish.
We need a graphic design that shows our PROCESS, called a "pipeline," that is creating future leaders. We are a US-based non-profit that operates a Christian school in rural Tanzania for 600 students (pre-K through 12th grade). It starts with child sponsorship program that allows poor children and orphans to attend school, we have a primary school (like USA elementary school, pre-K thru 7th), and are building a secondary boarding school (like USA middle and high school, grades 8-12), where students will live on campus in dormitories. We offer education, scholarships, leadership development experiences, help finding and securing college scholarships, academic and career counseling, placements for internships and jobs, and networking and leadership development content and events to create the next generation of servant leaders for the country. Prominent colors should probably be the green, blue and black in the Tanzania flag; we want the design to communicate "smart" and "strategic." The stages of the pipeline need to be properly named; we need to show a "leak" in the pipeline after the primary school because we currently have to send our students AWAY to other boarding schools because we don't have one. As the attached recording says, this is bad for their progress. The attached pipeline graphic is very rough and NOT meant to be imitated. It is factually correct, but is busy and not attractive.

Target Market(s)

Major financial contributors and foundations that want to give money to the cause

Industry/Entity Type

non-profit/Christian ministry in education

Font styles to use
Sans Serif

Requirements
Must have
• A "smart" and strategic" feel; preferably visible when on a half page
Nice to have
• a smart, sophisticated, serious look and feel
Should not have
• an elementary school feel

```html
<!DOCTYPE html>
<html lang="en">
<head>
<meta charset="UTF-8">
<title>KELIMO Strategic Leadership Pipeline</title>
<link rel="stylesheet" href="https://fonts.googleapis.com/css2?family=Montserrat:wght@500;600;700;800&display=swap">
<style>
  :root{
    --bg:#e5e5e5;
    --panel:#ffffff;
    --green:#3cb44a;
    --blue:#4aa3df;
    --yellow:#f1cc0b;
    --ink:#0d0d0d;
    --muted:#4a4a4a;
    --pipe:#bcd6e8;
    --leak:#4aa3df;
  }
  html,body{margin:0;padding:0;width:1199px;height:1200px;overflow:hidden;background:var(--bg);}
  body{font-family:"Montserrat",Arial,sans-serif;color:var(--ink);}
  .stage{position:absolute;left:0;top:0;width:1484px;height:1484px;transform:scale(0.80795);transform-origin:0 0;}
  .panel{position:absolute;left:56px;top:415px;width:1371px;height:654px;background:var(--panel);}
  .title{position:absolute;left:92px;top:452px;margin:0;font-size:39px;font-weight:800;letter-spacing:.3px;white-space:nowrap;line-height:48px;}
  .title .t-green{color:var(--green)} .title .t-blue{color:var(--blue)} .title .t-yellow{color:var(--yellow)} .title .t-black{color:var(--ink)}
  .subtitle{position:absolute;left:94px;top:503px;margin:0;font-size:18px;font-weight:600;color:var(--muted);line-height:24px;white-space:nowrap;}
  .brand{position:absolute;right:96px;top:454px;font-size:39px;font-weight:800;color:var(--green);line-height:48px;letter-spacing:.5px;}
  .pipework{position:absolute;left:0;top:0;width:1484px;height:1484px;}
  .photo{position:absolute;width:110px;height:73px;border:3px solid var(--blue);border-radius:4px;}
  .photo.tone-1{background:linear-gradient(135deg,#eef0f0,#c9a88f)}
  .photo.tone-2{background:linear-gradient(135deg,#7fa36a,#3e6b3c)}
  .photo.tone-3{background:linear-gradient(135deg,#9bb0c4,#c0464a)}
  .photo.tone-4{background:linear-gradient(135deg,#d8343a,#6d6a66)}
  .photo.tone-5{background:linear-gradient(135deg,#e8e8e8,#3b2a22)}
  .photo.tone-6{background:linear-gradient(135deg,#8a9b86,#5b5450)}
  .photo.tone-7{background:linear-gradient(135deg,#f2eeee,#9b3a38)}
  .stage-label{position:absolute;width:120px;text-align:center;font-size:14px;font-weight:700;line-height:16px;}
  .outcome{position:absolute;width:130px;border:3px solid var(--ink);border-radius:5px;background:var(--blue);overflow:hidden;}
  .outcome h3{margin:0;background:var(--yellow);font-size:18px;font-weight:800;text-align:center;line-height:24px;border-bottom:2px solid var(--ink);letter-spacing:.3px;}
  .outcome p{margin:0;padding:3px 2px 4px;font-size:13px;font-weight:700;text-align:center;line-height:15.3px;}
  .leak-note{position:absolute;left:420px;top:700px;width:62px;text-align:center;font-size:11px;font-weight:700;line-height:13px;color:var(--blue);}
</style>
</head>
<body>
<div class="stage">
  <div class="panel"></div>
  <h1 class="title"><span class="t-green">KELIMO</span> <span class="t-blue">Strategic</span> <span class="t-yellow">Leadership</span> <span class="t-black">Pipeline</span></h1>
  <p class="subtitle">Developing a steady flow of servant leaders for Tanzania's future</p>
  <div class="brand">KELIMO</div>

  <svg class="pipework" viewBox="0 0 1484 1484" aria-hidden="true">
    <g fill="none" stroke="var(--pipe)" stroke-width="10" stroke-linejoin="round">
      <path d="M225 590 H256 V633 H296"/>
      <path d="M418 633 H449 V590 H489"/>
      <path d="M611 590 H642 V633 H682"/>
      <path d="M804 633 H835 V590 H875"/>
      <path d="M997 590 H1028 V633 H1068"/>
      <path d="M1190 633 H1221 V590 H1261"/>
    </g>
    <g fill="var(--green)">
      <rect x="224" y="578" width="5" height="24"/><rect x="292" y="621" width="5" height="24"/>
      <rect x="417" y="621" width="5" height="24"/><rect x="485" y="578" width="5" height="24"/>
      <rect x="610" y="578" width="5" height="24"/><rect x="678" y="621" width="5" height="24"/>
      <rect x="803" y="621" width="5" height="24"/><rect x="871" y="578" width="5" height="24"/>
      <rect x="996" y="578" width="5" height="24"/><rect x="1064" y="621" width="5" height="24"/>
      <rect x="1189" y="621" width="5" height="24"/><rect x="1257" y="578" width="5" height="24"/>
    </g>
    <g class="leak">
      <path d="M443 636 L447 641 L443 646" fill="none" stroke="var(--panel)" stroke-width="2"/>
      <path d="M452 652 q-4 7 0 10 q4 -3 0 -10z" fill="var(--leak)"/>
      <path d="M449 668 q-4 7 0 10 q4 -3 0 -10z" fill="var(--leak)"/>
      <path d="M454 683 q-3.5 6 0 9 q3.5 -3 0 -9z" fill="var(--leak)" opacity=".7"/>
    </g>
    <g id="step-a">
      <rect x="156" y="633" width="15" height="34" fill="var(--pipe)"/>
      <rect x="152" y="632" width="23" height="5" fill="var(--green)"/>
      <path d="M121 693 A46 46 0 0 1 205 693" fill="none" stroke="var(--green)" stroke-width="3"/>
      <path d="M121 750 A46 46 0 0 0 205 750" fill="none" stroke="var(--blue)" stroke-width="3"/>
      <rect x="156" y="775" width="15" height="36" fill="var(--pipe)"/>
      <rect x="152" y="774" width="23" height="5" fill="var(--blue)"/>
    </g>
    <use href="#step-a" x="386"/>
    <use href="#step-a" x="771"/>
    <use href="#step-a" x="1157"/>
    <use href="#step-a" x="193" y="43"/>
    <use href="#step-a" x="578" y="43"/>
    <use href="#step-a" x="964" y="43"/>
  </svg>
  <div class="leak-note">Leak: sent away</div>

  <div class="photo tone-1" role="img" aria-label="Portrait of a young sponsored child" style="left:105px;top:551px"></div>
  <div class="photo tone-2" role="img" aria-label="Primary school pupils in uniform" style="left:298px;top:594px"></div>
  <div class="photo tone-3" role="img" aria-label="Secondary school students in a group" style="left:491px;top:551px"></div>
  <div class="photo tone-4" role="img" aria-label="Service leadership activity with children" style="left:684px;top:594px"></div>
  <div class="photo tone-5" role="img" aria-label="Graduate in cap and gown" style="left:876px;top:551px"></div>
  <div class="photo tone-6" role="img" aria-label="Group of young professionals" style="left:1069px;top:594px"></div>
  <div class="photo tone-7" role="img" aria-label="Collage of community leaders" style="left:1262px;top:551px"></div>

  <div class="stage-label" style="left:103px;top:697px">KELIMO<br>Sponsoreship<br>Program</div>
  <div class="stage-label" style="left:296px;top:740px">KELIMO<br>Primary<br>School</div>
  <div class="stage-label" style="left:489px;top:698px">KELIMO<br>Secondary<br>School</div>
  <div class="stage-label" style="left:681px;top:729px">KELIMO<br>Service<br>Leadership<br>Experience</div>
  <div class="stage-label" style="left:874px;top:689px">KELIMO<br>Higher<br>Education<br>Support</div>
  <div class="stage-label" style="left:1067px;top:741px">KELIMO<br>Employment<br>Center</div>
  <div class="stage-label" style="left:1260px;top:698px">KELIMO<br>Leadership<br>Hub</div>

  <div class="outcome" style="left:95px;top:815px"><h3>OUTCOME</h3><p>Close early development gap</p></div>
  <div class="outcome" style="left:288px;top:858px"><h3>OUTCOME</h3><p>Potential learders with Biblical Worldwide and strong academic foundations</p></div>
  <div class="outcome" style="left:481px;top:815px"><h3>OUTCOME</h3><p>Emerging leaders with concrete skills and strong servant mindset</p></div>
  <div class="outcome" style="left:674px;top:858px"><h3>OUTCOME</h3><p>Growing servant leaders with practical experience to effect change for the Kingdom</p></div>
  <div class="outcome" style="left:866px;top:815px"><h3>OUTCOME</h3><p>Expanding vision, capability, and motivation to solve bigger challenges for the nation</p></div>
  <div class="outcome" style="left:1059px;top:858px"><h3>OUTCOME</h3><p>Capable Christ-centered leaders in the marketplace, as value adding employees and entrepreneurs</p></div>
  <div class="outcome" style="left:1252px;top:815px"><h3>OUTCOME</h3><p>Mature Christian leaders being placed and positioned for leadership roles in the community and nation</p></div>
</div>
</body>
</html>
```